Project Sign for Construction Company

Site contractor needs a 4'x8' sign to place on construction sites for advertising. Our company builds the infrastructure for new housing developments. These sign will be posted on the road side to be viewed by passing cars. I want a clean and bold look and feel that resembles my company logo.

Font styles to use
Other font styles liked:
• Hypatia Sans Pro

Colors

Designer to choose colors to be used in the design.

Requirements
Must have
• 555-382-9146 | Info@MarlowPaving.example
• CUC 8047319
• www.MarlowPaving.example
• Services
• Road Construction
• Site Preparation & Excavation
• Underground Utilities
• Shoreline Restoration
Nice to have
• Now Hiring
• Pipe Layers
• Foremen
• Equipment Operators
Should not have
• Should not have stock picture images used in the design, focus on logo and geometric shapes

```html
<!DOCTYPE html>
<html lang="en">
<head>
<meta charset="utf-8">
<title>Marlow Paving – Roadside Banner</title>
<link rel="stylesheet" href="https://fonts.googleapis.com/css2?family=Saira:wght@400;500;700;800&display=swap">
<style>
  :root {
    --brand-blue: #0a4fa3;
    --ink: #1d1f24;
    --muted-gray: #8a8d92;
    --rule-gray: #c9cbce;
    --paper: #ffffff;
    --backdrop: #e8ecf1;
  }
  * { box-sizing: border-box; margin: 0; padding: 0; }
  html, body { width: 1200px; height: 900px; overflow: hidden; }
  body {
    background: var(--backdrop);
    font-family: "Saira", "Helvetica Neue", Arial, sans-serif;
    position: relative;
  }
  .banner {
    position: absolute;
    left: 410px; top: 20px;
    width: 380px; height: 860px;
    background: var(--paper);
    box-shadow: 0 6px 24px rgba(0,0,0,.12);
    overflow: hidden;
  }
  .frame-line { position: absolute; background: var(--rule-gray); }
  .frame-top { left: 18px; right: 18px; top: 15px; height: 1.5px; }
  .frame-left { left: 18px; top: 15px; bottom: 102px; width: 1.5px; }
  .frame-right { right: 18px; top: 15px; bottom: 102px; width: 1.5px; }
  .accent-bar { position: absolute; left: 0; top: 27px; width: 104px; height: 4px; background: var(--muted-gray); }
  .accent-tab { position: absolute; left: 0; top: 34px; width: 68px; height: 18px; background: var(--brand-blue);
    clip-path: polygon(0 0, 100% 0, 78% 100%, 0 100%); }
  .brand {
    position: absolute; left: 0; right: 0; top: 196px;
    display: flex; align-items: center; justify-content: center; gap: 10px;
  }
  .brand-mark { width: 20px; height: 20px; background: var(--brand-blue); flex: none; }
  .brand-name { color: var(--brand-blue); font-weight: 700; font-size: 30px; letter-spacing: 1px; line-height: 1; white-space: nowrap; }
  .headline { position: absolute; left: 0; right: 0; top: 276px; text-align: center; }
  .headline-kicker { color: var(--muted-gray); font-weight: 700; font-size: 18px; letter-spacing: .3px; line-height: 1; }
  .headline-main { color: var(--brand-blue); font-weight: 800; font-size: 33px; line-height: 34px; margin-top: 6px; letter-spacing: .2px; }
  .services-pill {
    position: absolute; left: 68px; width: 244px; top: 410px; height: 48px;
    border-radius: 24px; background: var(--brand-blue); color: var(--paper);
    display: flex; align-items: center; justify-content: center;
    font-weight: 500; font-size: 26px; letter-spacing: .5px;
  }
  .service-list { position: absolute; left: 64px; top: 500px; list-style: none; }
  .service-item { display: flex; align-items: flex-start; gap: 20px; color: var(--ink);
    font-size: 20px; font-weight: 500; line-height: 25px; margin-bottom: 25px; }
  .service-bullet { width: 14px; height: 14px; margin-top: 5px; border: 1.5px solid var(--brand-blue); flex: none; }
  .footer-rule { position: absolute; right: 0; bottom: 106px; width: 94px; height: 4px; background: var(--muted-gray); }
  .contact-band {
    position: absolute; left: 0; right: 0; bottom: 0; height: 102px;
    background: var(--brand-blue); color: var(--paper);
  }
  .call-label { position: absolute; left: 24px; top: 14px; font-size: 15px; line-height: 1; }
  .call-phone { position: absolute; left: 24px; top: 30px; font-size: 24px; font-weight: 500; line-height: 1.1; white-space: nowrap; }
  .call-web { position: absolute; left: 26px; top: 64px; font-size: 11px; line-height: 1; white-space: nowrap; }
  .contact-details { position: absolute; left: 204px; top: 32px; list-style: none; font-size: 10.5px; white-space: nowrap; }
  .contact-details li { display: flex; align-items: center; gap: 5px; height: 14px; margin-bottom: 11px; }
  .contact-details svg { width: 12px; height: 13px; flex: none; }
</style>
</head>
<body>
  <main class="banner">
    <div class="frame-line frame-top"></div>
    <div class="frame-line frame-left"></div>
    <div class="frame-line frame-right"></div>
    <div class="accent-bar"></div>
    <div class="accent-tab"></div>

    <div class="brand">
      <span class="brand-mark"></span>
      <span class="brand-name">MARLOW PAVING</span>
    </div>

    <header class="headline">
      <p class="headline-kicker">BUILDS THE INFRASTRUCTURE</p>
      <h1 class="headline-main">FOR NEW HOUSING<br>DEVELOPMENTS</h1>
    </header>

    <div class="services-pill">OUR SERVICES</div>

    <ul class="service-list">
      <li class="service-item"><span class="service-bullet"></span><span>Road Construction</span></li>
      <li class="service-item"><span class="service-bullet"></span><span>Site Preparation<br>&amp; Excavation</span></li>
      <li class="service-item"><span class="service-bullet"></span><span>Underground Utilities</span></li>
      <li class="service-item"><span class="service-bullet"></span><span>Shoreline Restoration</span></li>
    </ul>

    <div class="footer-rule"></div>

    <footer class="contact-band">
      <p class="call-label">CALL US NOW</p>
      <p class="call-phone">555-382-9146</p>
      <p class="call-web">www.MarlowPaving.example</p>
      <ul class="contact-details">
        <li>
          <svg viewBox="0 0 12 13" aria-hidden="true"><path d="M6 1a3.5 3.5 0 0 0-3.5 3.5C2.5 7 6 10 6 10s3.5-3 3.5-5.5A3.5 3.5 0 0 0 6 1z" fill="none" stroke="#fff" stroke-width="1.3"/><circle cx="6" cy="4.5" r="1.2" fill="#fff"/><path d="M1 12h10" stroke="#fff" stroke-width="1.3"/></svg>
          <span>CUC 8047319</span>
        </li>
        <li>
          <svg viewBox="0 0 12 13" aria-hidden="true"><rect x="1" y="3" width="10" height="7" fill="none" stroke="#fff" stroke-width="1.2"/><path d="M1 3l5 4 5-4M1 10l3.5-3.5M11 10L7.5 6.5" fill="none" stroke="#fff" stroke-width="1"/></svg>
          <span>Info@MarlowPaving.example</span>
        </li>
      </ul>
    </footer>
  </main>
</body>
</html>
```